Harbourline Bathrooms Business Card Design

Under Logo i would like our slogan: Quality bathrooms made affordable. Also on the card i would like: Free no obligation quotes. Our company is a bathroom renovation company.

Industry/Entity Type

Business

Contact Information for Business Card

Mark Pellowe, Mark@harbourlinebathrooms.co.nz, 021 473 2951, 0800 47 TUBS www.harbourlinebathrooms.co.nz

Requirements
Must have
• Include my logo. Green colours used

```html
<!DOCTYPE html>
<html lang="en">
<head>
<meta charset="utf-8">
<title>Harbourline Bathrooms – Business Card</title>
<link rel="stylesheet" href="https://fonts.googleapis.com/css2?family=Montserrat:wght@700&family=Quicksand:wght@400;500;600&display=swap">
<style>
  :root {
    --page-bg: #e9e9ea;
    --card-black: #0b0b0c;
    --card-charcoal: #2a2a2d;
    --card-white: #f7f7f7;
    --card-grey: #e2e2e3;
    --accent-green: #4cb860;
    --ink-dark: #2b2b2d;
    --ink-mid: #3d3d40;
    --divider: #bdbdbf;
    --white: #ffffff;
  }
  * { margin: 0; padding: 0; box-sizing: border-box; }
  html, body { width: 1200px; height: 1000px; overflow: hidden; }
  body { background: var(--page-bg); font-family: "Quicksand", sans-serif; position: relative; }

  .business-card {
    position: absolute; left: 100px; top: 210px;
    width: 1000px; height: 580px;
    border-radius: 6px; overflow: hidden;
    box-shadow: 0 14px 40px rgba(0,0,0,0.22);
    background: var(--card-white);
  }
  .card-shapes { position: absolute; inset: 0; }

  .brand-mark {
    position: absolute; left: 128px; top: 193px;
    width: 124px; height: 124px; border-radius: 50%;
    border: 10px solid var(--accent-green);
    background: var(--card-black);
  }
  .brand-rule {
    position: absolute; left: 284px; top: 172px;
    width: 2px; height: 120px; background: var(--accent-green);
  }
  .brand-block { position: absolute; left: 302px; top: 160px; }
  .brand-name {
    color: var(--white); font-weight: 400;
    font-size: 46px; line-height: 1; letter-spacing: 1px;
    text-transform: uppercase;
  }
  .brand-name span { display: block; font-size: 22px; letter-spacing: 11px; margin-top: 8px; }
  .brand-slogan {
    color: var(--white); font-weight: 500; font-size: 17px;
    margin-top: 10px; letter-spacing: 0.2px;
  }

  .holder-name {
    position: absolute; left: 86px; top: 398px;
    font-family: "Montserrat", sans-serif; font-weight: 700;
    font-size: 33px; line-height: 40px; color: var(--ink-dark);
  }
  .free-quotes {
    position: absolute; left: 86px; top: 452px;
    font-size: 17px; font-weight: 600; line-height: 22px;
    color: var(--accent-green); letter-spacing: 0.4px;
  }
  .contact-rule {
    position: absolute; left: 392px; top: 356px;
    width: 1px; height: 90px; background: var(--divider);
  }
  .contact-list { position: absolute; left: 412px; top: 338px; list-style: none; }
  .contact-list li {
    display: flex; align-items: center; gap: 10px;
    font-size: 26px; color: var(--ink-mid); line-height: 44px;
    white-space: nowrap;
  }
  .contact-icon { width: 26px; height: 26px; flex: none; }
  .website {
    position: absolute; right: 40px; top: 462px;
    font-size: 26px; line-height: 32px; color: var(--ink-mid); letter-spacing: 0.3px;
    white-space: nowrap;
  }
</style>
</head>
<body>
  <main class="business-card">
    <svg class="card-shapes" width="1000" height="580" viewBox="0 0 1000 580" aria-hidden="true">
      <defs>
        <radialGradient id="darkPanel" cx="0.5" cy="0.45" r="0.6">
          <stop offset="0" stop-color="#2a2a2d"/>
          <stop offset="1" stop-color="#0b0b0c"/>
        </radialGradient>
        <linearGradient id="lightPanel" x1="0" y1="0" x2="1" y2="1">
          <stop offset="0" stop-color="#e2e2e3"/>
          <stop offset="0.5" stop-color="#f7f7f7"/>
          <stop offset="1" stop-color="#e2e2e3"/>
        </linearGradient>
      </defs>
      <rect class="light-panel" width="1000" height="580" fill="url(#lightPanel)"/>
      <path class="accent-sweep" d="M0 0 H1000 V232 Q600 272 0 394 Z" fill="#4cb860"/>
      <path class="dark-panel" d="M0 0 H1000 V220 Q600 260 0 380 Z" fill="url(#darkPanel)"/>
      <rect class="accent-bar-right" x="810" y="300" width="190" height="9" fill="#4cb860"/>
      <rect class="accent-bar-left" x="0" y="505" width="440" height="9" fill="#4cb860"/>
      <rect class="accent-bar-bottom" x="0" y="556" width="1000" height="6" fill="#4cb860"/>
    </svg>

    <div class="brand-mark"></div>
    <div class="brand-rule"></div>
    <div class="brand-block">
      <p class="brand-name">Harbourline<span>Bathrooms</span></p>
      <p class="brand-slogan">Quality bathrooms made affordable</p>
    </div>

    <p class="holder-name">Mark Pellowe</p>
    <p class="free-quotes">Free no obligation quotes</p>
    <div class="contact-rule"></div>
    <ul class="contact-list">
      <li>
        <svg class="contact-icon" viewBox="0 0 26 26" aria-hidden="true">
          <circle cx="13" cy="13" r="13" fill="#4cb860"/>
          <path d="M9 7c1 0 1.6 2.4 1.2 3.2-.4.6-1 .8-.6 1.8.6 1.4 1.6 2.6 3 3.4.8.4 1.2-.2 1.8-.6.8-.4 3 .6 3 1.6 0 1.6-1.8 2.6-3.4 2-3.6-1.2-6.4-4.2-7.2-7.8C6.4 9 7.6 7 9 7z" fill="#ffffff"/>
        </svg>
        <span>021 473 2951 &nbsp;0800 47 TUBS</span>
      </li>
      <li>
        <svg class="contact-icon" viewBox="0 0 26 26" aria-hidden="true">
          <circle cx="13" cy="13" r="13" fill="#4cb860"/>
          <rect x="6.5" y="8.5" width="13" height="9" rx="1" fill="#ffffff"/>
          <path d="M6.8 9 L13 13.6 L19.2 9" fill="none" stroke="#4cb860" stroke-width="1.4"/>
        </svg>
        <span>mark@harbourlinebathrooms.co.nz</span>
      </li>
    </ul>
    <p class="website">www.harbourlinebathrooms.co.nz</p>
  </main>
</body>
</html>
```